Velbrook App Homepage Design making customers feel in control of their spend

Hi,
We need a App Homepage design with a UI similar to the attached mock up on an Quillo 4. The app is intended to put customers in control of their usage and spend on their fixed phone, broadband, mobile, gas and electricity.

Please fee free to propose improvements to the background images, icons, colours, etc.

Any questions please let me know.

Thanks
Tomasz

Target Market(s)

Consumer customers

Industry/Entity Type

Internet

Font styles to use
Sans Serif

Colors
3276b5
0255a3
85acd3
cfdeed
ffffff

Requirements
Must have
• Content in line with the guidelines in the attached mock up

```html
<!DOCTYPE html>
<html lang="en">
<head>
<meta charset="utf-8">
<title>Velbrook App Homepage</title>
<link href="https://fonts.googleapis.com/css2?family=Open+Sans:wght@300;400;600;700&display=swap" rel="stylesheet">
<style>
  :root {
    --bg-top: #3a7f9c;
    --bg-bottom: #245a78;
    --header: #3f6f82;
    --greeting: #4f8ea5;
    --photo-a: #6fa9bd;
    --photo-b: #3f7f98;
    --tile-a: #4a86ad;
    --tile-b: #5d9fd1;
    --support-a: #7fe0e0;
    --support-b: #5aa8e6;
    --white: #ffffff;
    --ink: #1f3346;
    --mint: #8fe0b8;
    --sky: #5aa6ea;
    --flame: #e0403a;
    --lime: #58cf3a;
    --violet: #a24ae0;
  }
  * { box-sizing: border-box; margin: 0; padding: 0; }
  html, body { width: 1200px; height: 1200px; overflow: hidden; }
  body {
    font-family: "Open Sans", Arial, sans-serif;
    background: linear-gradient(160deg, var(--bg-top), var(--bg-bottom));
    position: relative;
    color: var(--white);
  }
  .brand-lockup {
    position: absolute; left: 150px; top: 920px;
    display: flex; align-items: center; gap: 22px;
  }
  .brand-dot { width: 72px; height: 72px; border-radius: 50%; background: var(--white); }
  .brand-name { font-size: 56px; font-weight: 600; color: var(--white); letter-spacing: 1px; }

  .app-screen {
    position: absolute; left: 640px; top: 150px;
    width: 440px; height: 800px;
    display: flex; flex-direction: column;
    box-shadow: 0 30px 60px rgba(0,0,0,.3);
    overflow: hidden;
  }
  .app-header {
    height: 64px; background: var(--header);
    display: flex; align-items: center; justify-content: center; position: relative;
  }
  .menu-icon { position: absolute; left: 20px; top: 22px; }
  .app-title { font-size: 24px; font-weight: 600; }
  .greeting {
    height: 110px; background: var(--greeting);
    text-align: center; padding-top: 24px;
  }
  .greeting h1 { font-size: 28px; font-weight: 300; }
  .greeting h1 strong { font-weight: 600; }
  .greeting p { font-size: 16px; font-weight: 300; margin-top: 4px; }
  .usage-area {
    flex: 1; position: relative;
    background: linear-gradient(170deg, var(--photo-a), var(--photo-b));
  }
  .usage-dial { position: absolute; left: 110px; top: 105px; width: 220px; height: 220px; }
  .dial-label {
    position: absolute; left: 110px; top: 105px; width: 220px; height: 220px;
    display: flex; flex-direction: column; align-items: center; justify-content: center;
    color: var(--ink);
  }
  .dial-label small { font-size: 12px; font-weight: 600; }
  .dial-label span { font-size: 48px; font-weight: 400; line-height: 1.1; }
  .service-bubble {
    position: absolute; width: 56px; height: 56px; border-radius: 50%;
    display: flex; align-items: center; justify-content: center;
  }
  .bubble-phone { left: 40px; top: 120px; background: var(--mint); }
  .bubble-energy { left: 260px; top: 28px; background: var(--sky); }
  .bubble-gas { left: 356px; top: 110px; background: var(--flame); }
  .bubble-mobile { left: 320px; top: 320px; background: var(--lime); }
  .bubble-broadband { left: 44px; top: 270px; background: var(--violet); }
  .summary-tiles { display: flex; height: 130px; }
  .summary-tile {
    flex: 1; background: linear-gradient(135deg, var(--tile-a), var(--tile-b));
    display: flex; flex-direction: column; align-items: center; justify-content: center;
    border-right: 1px solid rgba(255,255,255,.15);
  }
  .summary-tile strong { font-size: 30px; font-weight: 400; }
  .summary-tile span { font-size: 14px; font-weight: 300; text-align: center; line-height: 1.3; }
  .support-bar {
    height: 74px; background: linear-gradient(90deg, var(--support-a), var(--support-b));
    display: flex; align-items: center; justify-content: center;
    color: var(--ink); font-size: 22px; font-weight: 700; letter-spacing: 1px;
  }
</style>
</head>
<body>
  <div class="brand-lockup">
    <div class="brand-dot"></div>
    <div class="brand-name">Velbrook</div>
  </div>

  <main class="app-screen">
    <header class="app-header">
      <svg class="menu-icon" width="26" height="20" viewBox="0 0 26 20"><g stroke="#fff" stroke-width="2.5" stroke-linecap="round"><line x1="2" y1="3" x2="24" y2="3"/><line x1="2" y1="10" x2="20" y2="10"/><line x1="2" y1="17" x2="16" y2="17"/></g></svg>
      <div class="app-title">Velbrook</div>
    </header>
    <section class="greeting">
      <h1>Good Morning <strong>Maren</strong></h1>
      <p>Welcome to Velbrook</p>
    </section>
    <section class="usage-area" role="img" aria-label="Background photo of a woman relaxing at home with a laptop">
      <svg class="usage-dial" viewBox="0 0 220 220">
        <circle cx="110" cy="110" r="100" fill="#fff"/>
        <g fill="none" stroke-width="7" transform="rotate(-90 110 110)">
          <circle cx="110" cy="110" r="104" stroke="#7fd8ea" stroke-dasharray="163 491"/>
          <circle cx="110" cy="110" r="104" stroke="#e0403a" stroke-dasharray="0 163 260 231"/>
          <circle cx="110" cy="110" r="104" stroke="#58cf3a" stroke-dasharray="0 423 100 131"/>
          <circle cx="110" cy="110" r="104" stroke="#a24ae0" stroke-dasharray="0 523 40 91"/>
          <circle cx="110" cy="110" r="104" stroke="#5aa6ea" stroke-dasharray="0 563 91"/>
        </g>
      </svg>
      <div class="dial-label"><small>You current total charges</small><span>£68.39</span></div>

      <div class="service-bubble bubble-phone"><svg width="24" height="24" viewBox="0 0 24 24"><path d="M5 4l4 0 2 5-2.5 1.5a11 11 0 0 0 5 5L15 13l5 2v4a2 2 0 0 1-2 2A16 16 0 0 1 3 6a2 2 0 0 1 2-2z" fill="#fff"/></svg></div>
      <div class="service-bubble bubble-energy"><svg width="24" height="24" viewBox="0 0 24 24"><path d="M12 2a7 7 0 0 0-4 12.7V18h8v-3.3A7 7 0 0 0 12 2z" fill="#fff"/><rect x="9" y="19.5" width="6" height="2.5" rx="1" fill="#fff"/></svg></div>
      <div class="service-bubble bubble-gas"><svg width="24" height="24" viewBox="0 0 24 24"><path d="M12 2c1 4 6 6 6 12a6 6 0 0 1-12 0c0-3 2-4 2-6 2 1 3 3 3 3 1-3 0-6 1-9z" fill="#fff"/></svg></div>
      <div class="service-bubble bubble-mobile"><svg width="24" height="24" viewBox="0 0 24 24"><rect x="7" y="2" width="10" height="20" rx="2" fill="none" stroke="#fff" stroke-width="2"/><circle cx="12" cy="18" r="1.2" fill="#fff"/></svg></div>
      <div class="service-bubble bubble-broadband"><svg width="24" height="24" viewBox="0 0 24 24"><circle cx="12" cy="12" r="9" fill="none" stroke="#fff" stroke-width="2"/><path d="M3 12h18M12 3c-3 3-3 15 0 18M12 3c3 3 3 15 0 18" fill="none" stroke="#fff" stroke-width="1.5"/></svg></div>
    </section>
    <section class="summary-tiles">
      <div class="summary-tile"><strong>£75.76</strong><span>Last bill</span></div>
      <div class="summary-tile"><strong>9/12/2016</strong><span>Allowance renews in<br>18 days</span></div>
    </section>
    <footer class="support-bar">24/7 SUPPORT</footer>
  </main>
</body>
</html>
```